GKL Auto - help to get me noticed

We not long ago tasked Pixel Harbor to design a logo for my business. I'm happy with the result so would like to have a business card designed as a follow up.

It's an Automotive service and repair business that offers the following -
- Servicing
- General repairs
- Brakes
- Detailing
- Integrity

GKL Automotive
Malcolm Pryde
0491 726 183

Target Market(s)

Everyday people with the ability to reach out to corporate customers also.

Industry/Entity Type

Automotive

Contact Information for Business Card

Black card, logo, name and phone number on front. Other details on back of card.

```html
<!DOCTYPE html>
<html lang="en">
<head>
<meta charset="UTF-8">
<title>GKL Automotive – Business Card</title>
<link href="https://fonts.googleapis.com/css2?family=Inter:wght@400;500&display=swap" rel="stylesheet">
<style>
  :root {
    --backdrop: #2b2c2e;
    --card: #0a0b0d;
    --ink: #f2f2f2;
    --accent: #8cc63f;
    --shadow: rgba(0, 0, 0, 0.55);
  }
  * { margin: 0; padding: 0; box-sizing: border-box; }
  html, body {
    width: 1200px;
    height: 800px;
    overflow: hidden;
    background: var(--backdrop);
    font-family: "Inter", Arial, sans-serif;
  }
  .canvas {
    position: relative;
    width: 1200px;
    height: 800px;
  }
  .card {
    position: absolute;
    width: 520px;
    height: 290px;
    background: var(--card);
    box-shadow: 0 18px 40px var(--shadow);
    color: var(--ink);
  }
  .card--front { left: 170px; top: 90px; }
  .card--back  { left: 510px; top: 420px; }

  .brand {
    position: absolute;
    left: 32px;
    top: 30px;
    display: flex;
    align-items: center;
    gap: 9px;
  }
  .brand__mark {
    width: 14px;
    height: 14px;
    background: var(--accent);
  }
  .brand__name {
    font-size: 15px;
    font-weight: 500;
    letter-spacing: 0.06em;
    text-transform: uppercase;
    color: var(--ink);
  }
  .holder-name {
    position: absolute;
    left: 92px;
    top: 120px;
    font-size: 24px;
    font-weight: 400;
    letter-spacing: 0.45em;
    text-transform: uppercase;
  }
  .holder-phone {
    position: absolute;
    right: 30px;
    top: 178px;
    font-size: 13px;
    letter-spacing: 0.3em;
  }
  .services {
    position: absolute;
    right: 30px;
    bottom: 26px;
    font-size: 11.5px;
    font-weight: 500;
    letter-spacing: 0.02em;
    text-transform: uppercase;
    white-space: nowrap;
  }
  .services__sep { margin: 0 4px; opacity: 0.8; }
</style>
</head>
<body>
  <main class="canvas">
    <section class="card card--front" aria-label="Business card front">
      <div class="brand">
        <span class="brand__mark"></span>
        <span class="brand__name">GKL Automotive</span>
      </div>
      <h1 class="holder-name">Malcolm Pryde</h1>
      <p class="holder-phone">0491 726 183</p>
    </section>

    <section class="card card--back" aria-label="Business card back">
      <p class="services">
        Brakes<span class="services__sep">|</span>Detailing<span class="services__sep">|</span>Integrity<span class="services__sep">|</span>Servicing<span class="services__sep">|</span>General Repairs
      </p>
    </section>
  </main>
</body>
</html>
```